Artisan Bread Company needs a business card

I need a business card design, for an artisan bread company called "Holloway's Bread".

I would like the logo on one side, and on the other, I would like it to say

Dorian Holloway
Baker
416.552.0193
hollowaysbread@breadmail.example

Not necessarily in that order- but it must have these.

Industry/Entity Type

Business

Font styles to use
Serif

Requirements
Must have
• The provided logo on the front, this on the back-
• Dorian Holloway
• Baker
• 416.552.0193
• hollowaysbread@breadmail.example

```html
<!DOCTYPE html>
<html lang="en">
<head>
<meta charset="utf-8">
<title>Holloway's Bread — Business Card</title>
<link rel="stylesheet" href="https://fonts.googleapis.com/css2?family=Josefin+Sans:wght@300;400&family=Pinyon+Script&display=swap">
<style>
  :root {
    --backdrop: #cbcbcb;
    --card: #ffffff;
    --card-back: #f6f6f6;
    --ink: #141414;
    --band: #0d0d0d;
    --stripe: #6e6e6e;
    --reverse: #ffffff;
  }
  * { box-sizing: border-box; margin: 0; padding: 0; }
  html, body {
    width: 1200px; height: 1004px; overflow: hidden;
    background: var(--backdrop);
  }
  .canvas {
    position: relative; width: 1200px; height: 1004px;
  }
  .card {
    position: absolute; left: 300px; width: 600px; height: 343px;
    overflow: hidden;
    box-shadow: 0 6px 14px rgba(0,0,0,0.18);
  }
  .card--front { top: 130px; background: var(--card); }
  .card--back { top: 533px; background: var(--card-back); }

  .wordmark {
    position: absolute;
    display: flex; align-items: center; gap: 12px;
    font-family: "Josefin Sans", sans-serif; font-weight: 300;
    color: var(--ink); letter-spacing: 0.06em; white-space: nowrap;
  }
  .wordmark__dot {
    width: 12px; height: 12px; border-radius: 50%; background: var(--ink);
  }
  .card--front .wordmark {
    left: 50%; top: 50%; transform: translate(-50%, -50%);
    font-size: 40px;
  }
  .card--back .wordmark {
    left: 60px; top: 128px; font-size: 30px;
  }

  .holder {
    position: absolute; right: 40px; top: 40px; text-align: right;
    color: var(--ink);
  }
  .holder__name {
    font-family: "Pinyon Script", cursive; font-size: 28px; line-height: 1;
  }
  .holder__role {
    font-family: "Josefin Sans", sans-serif; font-weight: 300;
    font-size: 12px; margin-top: 4px; margin-right: 14px;
  }

  .wave { position: absolute; left: 0; top: 0; }

  .contact {
    position: absolute; right: 28px; top: 252px; text-align: right;
    font-family: "Josefin Sans", sans-serif; font-weight: 300;
    font-size: 14px; color: var(--reverse); line-height: 26px;
  }
  .contact__line { display: flex; justify-content: flex-end; align-items: center; gap: 8px; white-space: nowrap; }
  .contact__icon { width: 13px; height: 13px; fill: var(--reverse); flex: none; }
</style>
</head>
<body>
<main class="canvas">

  <section class="card card--front" aria-label="Card front">
    <div class="wordmark"><span class="wordmark__dot"></span>Holloway's Bread</div>
  </section>

  <section class="card card--back" aria-label="Card back">
    <svg class="wave" width="600" height="343" viewBox="0 0 600 343" aria-hidden="true">
      <path d="M0 252 C 150 262, 300 240, 420 190 C 500 156, 560 140, 600 134 L600 150 C 540 158, 480 180, 410 210 C 300 255, 150 272, 0 268 Z" fill="var(--stripe)"/>
      <path d="M0 280 C 150 286, 310 262, 430 208 C 510 172, 560 158, 600 154 L600 343 L0 343 Z" fill="var(--band)"/>
    </svg>

    <div class="holder">
      <div class="holder__name">Dorian Holloway</div>
      <div class="holder__role">Baker</div>
    </div>

    <div class="wordmark"><span class="wordmark__dot"></span>Holloway's Bread</div>

    <div class="contact">
      <div class="contact__line">416.552.0193
        <svg class="contact__icon" viewBox="0 0 24 24" aria-hidden="true"><path d="M6.6 10.8a15 15 0 0 0 6.6 6.6l2.2-2.2a1 1 0 0 1 1-.25 11.4 11.4 0 0 0 3.6.57 1 1 0 0 1 1 1V20a1 1 0 0 1-1 1A17 17 0 0 1 3 4a1 1 0 0 1 1-1h3.5a1 1 0 0 1 1 1c0 1.25.2 2.45.57 3.57a1 1 0 0 1-.25 1z"/></svg>
      </div>
      <div class="contact__line">hollowaysbread@breadmail.example
        <svg class="contact__icon" viewBox="0 0 24 24" aria-hidden="true"><path d="M2 5h20v14H2z M3.5 6.5 12 13l8.5-6.5" fill="none" stroke="#fff" stroke-width="2"/></svg>
      </div>
    </div>
  </section>

</main>
</body>
</html>
```